Business card design for a engineering company

I need a double sided business card design for my company "Verdmont Flow Solutions". The card will be used in Malaysia. Sleek and professional, with a little design flare to it.
Information to showcase:
1. Company logo
2. Name, title, phone, email address, website address
3. our products "Pumping technology, Valve & actuation, Air Moving Technology
Example:
Ravi Tanaka
Business manager
ravi.tanaka@verdmont-example.com
www.verdmont-example.com.my
- Pumping technology
- Valve & actuation
- Air moving technology
Target Market(s)
engineers, purchasing managers
Industry/Entity Type
Business
Contact Information for Business Card
Ravi Tanaka
Business manager
ravi.tanaka@verdmont-example.com
www.verdmont-example.com.my
- Pumping technology
- Valve & actuation
- Air moving technology
catch phrase : "Solving flow challenges, exceeding expectations"

```html
<!DOCTYPE html>
<html lang="en">
<head>
<meta charset="utf-8">
<title>Verdmont Flow Solutions – Business Card Concepts</title>
<link href="https://fonts.googleapis.com/css2?family=Jost:wght@400;500;600&display=swap" rel="stylesheet">
<style>
  :root {
    --teal: #0b4b67;
    --teal-deep: #0c3244;
    --teal-light: #4f8aa6;
    --orange: #f07c22;
    --ink: #1f4e6b;
    --white: #ffffff;
    --page: #ffffff;
  }
  * { margin: 0; padding: 0; box-sizing: border-box; }
  html, body { width: 1200px; height: 424px; overflow: hidden; background: var(--page); }
  body { position: relative; font-family: "Jost", "Helvetica Neue", Arial, sans-serif; color: var(--ink); }

  .card { position: absolute; overflow: hidden; }
  .card svg.bg { position: absolute; inset: 0; }

  /* fronts */
  .front { top: 0; height: 202px; width: 354px; }
  .front-swoosh { left: 0; background: var(--white); }
  .front-panel { left: 424px; width: 352px; background: var(--teal); }
  .front-panel .sheet {
    position: absolute; left: 0; top: 0; width: 252px; height: 180px;
    background: var(--white); border-bottom-right-radius: 24px;
  }
  .front-gradient {
    left: 846px;
    background: radial-gradient(ellipse at 20% 100%, #08222e 0%, var(--teal-deep) 35%, #1d5470 70%, var(--teal-light) 100%);
  }

  .wordmark { position: absolute; display: flex; align-items: center; gap: 8px; color: var(--teal-deep); font-weight: 500; }
  .wordmark .dot { width: 30px; height: 30px; border-radius: 50%; background: var(--teal-deep); }
  .wordmark .name { line-height: 1; }
  .wordmark .name .big { display: block; font-size: 25px; letter-spacing: 0.5px; }
  .wordmark .name .small { display: block; font-size: 8px; letter-spacing: 3.2px; margin-top: 3px; }
  .wordmark.on-dark { color: var(--white); }
  .wordmark.on-dark .dot { background: var(--white); }

  .website { position: absolute; font-size: 7.5px; letter-spacing: 3px; color: var(--ink); white-space: nowrap; }
  .website.on-dark { color: var(--white); font-weight: 600; }

  /* backs */
  .back { top: 222px; height: 202px; width: 354px; }
  .back-1 { left: 0; }
  .back-2 { left: 424px; width: 352px; }
  .back-3 { left: 846px; }

  .products { position: absolute; list-style: none; color: var(--white); font-size: 7.5px; letter-spacing: 1.2px; }
  .products li { white-space: nowrap; }

  .contact { position: absolute; }
  .contact .person { font-size: 12.5px; letter-spacing: 1px; font-weight: 400; }
  .contact .role { font-size: 12px; letter-spacing: 1px; margin-top: 10px; }
  .contact .lines { list-style: none; margin-top: 12px; font-size: 6.8px; }
  .contact .lines li { display: flex; align-items: flex-start; gap: 12px; margin-bottom: 11px; line-height: 1.5; }
  .contact .lines svg { flex: none; width: 10px; height: 10px; margin-top: 1px; }

  .wordmark.mini .dot { width: 18px; height: 18px; }
  .wordmark.mini .name .big { font-size: 14px; }
  .wordmark.mini .name .small { font-size: 4.5px; letter-spacing: 2px; margin-top: 1px; }
</style>
</head>
<body>

<!-- Concept 1: front -->
<section class="card front front-swoosh">
  <svg class="bg" width="354" height="202" viewBox="0 0 354 202">
    <path d="M212 0 Q300 18 354 78 L354 0 Z" fill="var(--teal)"/>
    <path d="M214 0 Q302 20 354 80" fill="none" stroke="var(--orange)" stroke-width="2.5"/>
    <path d="M0 104 Q40 182 168 202 L0 202 Z" fill="var(--teal-deep)"/>
    <path d="M0 98 Q38 180 170 202" fill="none" stroke="var(--orange)" stroke-width="3"/>
  </svg>
  <div class="wordmark" style="left:86px; top:84px;">
    <span class="dot"></span>
    <span class="name"><span class="big">VERDMONT</span><span class="small">FLOW SOLUTIONS</span></span>
  </div>
  <p class="website" style="left:104px; top:136px;">www.verdmont-example.com.my</p>
</section>

<!-- Concept 2: front -->
<section class="card front front-panel">
  <div class="sheet"></div>
  <div class="wordmark" style="left:28px; top:80px;">
    <span class="dot"></span>
    <span class="name"><span class="big">VERDMONT</span><span class="small">FLOW SOLUTIONS</span></span>
  </div>
  <p class="website" style="left:28px; top:136px;">www.verdmont-example.com.my</p>
</section>

<!-- Concept 3: front -->
<section class="card front front-gradient">
  <div class="wordmark on-dark" style="left:96px; top:80px;">
    <span class="dot"></span>
    <span class="name"><span class="big">VERDMONT</span><span class="small">FLOW SOLUTIONS</span></span>
  </div>
  <p class="website on-dark" style="left:104px; top:136px;">www.verdmont-example.com.my</p>
</section>

<!-- Concept 1: back -->
<section class="card back back-1">
  <svg class="bg" width="354" height="202" viewBox="0 0 354 202">
    <defs>
      <linearGradient id="slab-1" x1="0" y1="0" x2="1" y2="1">
        <stop offset="0" stop-color="#0a2c3c"/>
        <stop offset="1" stop-color="#3f7a96"/>
      </linearGradient>
    </defs>
    <path d="M0 39 H156 Q166 39 168 48 L188 148 Q190 159 178 159 H0 Z" fill="url(#slab-1)"/>
  </svg>
  <ul class="products" style="left:36px; top:66px; line-height:25px;">
    <li>- Pumping technology</li>
    <li>- Valve &amp; actuation</li>
    <li>- Air moving technology</li>
  </ul>
  <div class="contact" style="left:208px; top:40px;">
    <p class="person">Ravi Tanaka</p>
    <p class="role">Business Manager</p>
    <ul class="lines">
      <li><svg viewBox="0 0 10 10"><rect x="0.5" y="2" width="9" height="6.5" fill="var(--orange)"/><path d="M0.5 2 L5 6 L9.5 2" fill="none" stroke="#fff" stroke-width="0.8"/></svg>ravi.tanaka@verdmont-example.com</li>
      <li><svg viewBox="0 0 10 10"><path d="M2 0.5 L4 2.5 L3 4 Q4.5 6.5 6 7 L7.5 6 L9.5 8 L8 9.5 Q3 9 0.5 2 Z" fill="var(--orange)"/></svg>03-5550 1942</li>
      <li><svg viewBox="0 0 10 10"><path d="M5 0.5 A3.5 3.5 0 0 1 8.5 4 Q8.5 6.5 5 9.8 Q1.5 6.5 1.5 4 A3.5 3.5 0 0 1 5 0.5 Z" fill="var(--orange)"/><circle cx="5" cy="4" r="1.4" fill="#fff"/></svg><span>12 Jalan Kiambang<br>Shah Alam 40150</span></li>
    </ul>
  </div>
  <div class="wordmark mini" style="left:126px; top:172px;">
    <span class="dot"></span>
    <span class="name"><span class="big">VERDMONT</span><span class="small">FLOW SOLUTIONS</span></span>
  </div>
</section>

<!-- Concept 2: back -->
<section class="card back back-2">
  <svg class="bg" width="352" height="202" viewBox="0 0 352 202">
    <path d="M0 0 H140 Q210 101 140 202 H0 Z" fill="var(--teal)"/>
  </svg>
  <ul class="products" style="left:38px; top:50px; line-height:42px;">
    <li>- Pumping technology</li>
    <li>- Valve &amp; actuation</li>
    <li>- Air moving technology</li>
  </ul>
  <div class="contact" style="left:211px; top:40px;">
    <p class="person">Ravi Tanaka</p>
    <p class="role">Business Manager</p>
    <ul class="lines">
      <li><svg viewBox="0 0 10 10"><rect x="0.5" y="2" width="9" height="6.5" fill="var(--orange)"/><path d="M0.5 2 L5 6 L9.5 2" fill="none" stroke="#fff" stroke-width="0.8"/></svg>ravi.tanaka@verdmont-example.com</li>
      <li><svg viewBox="0 0 10 10"><path d="M2 0.5 L4 2.5 L3 4 Q4.5 6.5 6 7 L7.5 6 L9.5 8 L8 9.5 Q3 9 0.5 2 Z" fill="var(--orange)"/></svg>03-5550 1942</li>
      <li><svg viewBox="0 0 10 10"><path d="M5 0.5 A3.5 3.5 0 0 1 8.5 4 Q8.5 6.5 5 9.8 Q1.5 6.5 1.5 4 A3.5 3.5 0 0 1 5 0.5 Z" fill="var(--orange)"/><circle cx="5" cy="4" r="1.4" fill="#fff"/></svg><span>12 Jalan Kiambang<br>Shah Alam 40150</span></li>
    </ul>
  </div>
</section>

<!-- Concept 3: back -->
<section class="card back back-3">
  <svg class="bg" width="354" height="202" viewBox="0 0 354 202">
    <defs>
      <linearGradient id="slab-3" x1="0" y1="0" x2="1" y2="1">
        <stop offset="0" stop-color="#0a2c3c"/>
        <stop offset="1" stop-color="#3f7a96"/>
      </linearGradient>
    </defs>
    <path d="M0 39 H162 L186 159 H0 Z" fill="url(#slab-3)"/>
  </svg>
  <ul class="products" style="left:42px; top:66px; line-height:25px;">
    <li>- Pumping technology</li>
    <li>- Valve &amp; actuation</li>
    <li>- Air moving technology</li>
  </ul>
  <div class="contact" style="left:210px; top:40px;">
    <p class="person">Ravi Tanaka</p>
    <p class="role">Business Manager</p>
    <ul class="lines">
      <li><svg viewBox="0 0 10 10"><rect x="0.5" y="2" width="9" height="6.5" fill="var(--orange)"/><path d="M0.5 2 L5 6 L9.5 2" fill="none" stroke="#fff" stroke-width="0.8"/></svg>ravi.tanaka@verdmont-example.com</li>
      <li><svg viewBox="0 0 10 10"><path d="M2 0.5 L4 2.5 L3 4 Q4.5 6.5 6 7 L7.5 6 L9.5 8 L8 9.5 Q3 9 0.5 2 Z" fill="var(--orange)"/></svg>03-5550 1942</li>
      <li><svg viewBox="0 0 10 10"><path d="M5 0.5 A3.5 3.5 0 0 1 8.5 4 Q8.5 6.5 5 9.8 Q1.5 6.5 1.5 4 A3.5 3.5 0 0 1 5 0.5 Z" fill="var(--orange)"/><circle cx="5" cy="4" r="1.4" fill="#fff"/></svg><span>12 Jalan Kiambang<br>Shah Alam 40150</span></li>
    </ul>
  </div>
  <div class="wordmark mini" style="left:128px; top:172px;">
    <span class="dot"></span>
    <span class="name"><span class="big">VERDMONT</span><span class="small">FLOW SOLUTIONS</span></span>
  </div>
</section>

</body>
</html>
```